Sri Lankan Cricket Tour For Girls Aged 14-18 in July 2018

We need a flyer to promote a cricket tour of Sri Lanka in July 2018 for girls aged 14-18.
We want the flyer to call for "expressions of interest".
We would like the Sri Lankan Flag also images of cricket ball and beaches and palm trees etc.
Mention Level 3 Coaches with International experience.
Target market is parents of girls aged 14 to 18 and girls aged 14 to 18

Target Market(s)

Parents of girls aged 14 to 18 and girls aged 14 to 18

Industry/Entity Type

Travel

Font styles to use
Serif
Sans Serif

Colors
0355a3
ec1f27
fbed22

Requirements
Must have
• Sri Lankan Flag, Halvey Athletics Logo, email address boyd@halveyathletics.com.au.
• - 10 Day Tour
• - Play on First Class Grounds
• - Level 3 Coaches With International Experience
• - For More Information Contact Boyd boyd@halveyathletics.com.au
Nice to have
• Picture of girls playing cricket, sun and beach
Should not have
• Cartoon type images
• Photo's of actual cricketers

```html
<!DOCTYPE html>
<html lang="en">
<head>
<meta charset="utf-8">
<title>Sri Lanka Girls Cricket Tour – Expressions of Interest</title>
<link href="https://fonts.googleapis.com/css2?family=Oswald:wght@500;600&family=Montserrat:wght@700;800&family=Archivo+Black&display=swap" rel="stylesheet">
<style>
  :root {
    --brand-blue: #0355a3;
    --bright-blue: #1a62c6;
    --brand-red: #ec1f27;
    --brand-yellow: #fbed22;
    --ink: #0d0d0d;
    --panel: #1b1b1b;
    --footer: #151515;
    --rule: #6a6a6a;
    --white: #ffffff;
    --flag-maroon: #8d153a;
    --flag-gold: #ffbe29;
    --flag-green: #00534e;
    --flag-orange: #eb7400;
  }
  * { margin: 0; padding: 0; box-sizing: border-box; }
  html, body { width: 849px; height: 1200px; overflow: hidden; background: var(--ink); }

  .flyer {
    position: relative;
    width: 849px;
    height: 1200px;
    overflow: hidden;
    background: var(--ink);
    font-family: "Montserrat", Arial, sans-serif;
    color: var(--white);
  }

  /* Hero imagery: scene, waving flag banner, players */
  .hero-scene {
    position: absolute;
    left: 0; top: 0;
    width: 849px; height: 780px;
    background: linear-gradient(180deg,
      #6f9bb4 0%, #4f8fb0 30%, #3f7f9c 40%,
      #2e5a45 50%, #1f3d2c 62%, #15211a 78%, var(--ink) 100%);
  }
  .hero-flag-banner {
    position: absolute;
    left: 0; top: 0;
    width: 849px; height: 300px;
    background:
      linear-gradient(180deg, rgba(0,0,0,0) 60%, rgba(111,155,180,1) 100%),
      linear-gradient(100deg, #e0701e 0%, #c8862a 14%, #a3233f 34%, #9a1d3c 60%, #c28a2c 82%, #a4263e 100%);
  }
  .hero-players {
    position: absolute;
    left: 95px; top: 150px;
    width: 420px; height: 400px;
    border-radius: 40% 40% 0 0 / 30% 30% 0 0;
    background: radial-gradient(ellipse at 50% 45%,
      rgba(46,74,140,.95) 0%, rgba(60,90,150,.75) 35%,
      rgba(40,60,90,.35) 65%, rgba(20,30,30,0) 100%);
  }

  .brand {
    position: absolute;
    left: 521px; top: 196px;
    width: 297px;
    display: flex;
    flex-direction: column;
    align-items: center;
    gap: 12px;
  }
  .brand-dot {
    width: 118px; height: 118px;
    border-radius: 50%;
    background: var(--brand-red);
  }
  .brand-name {
    font-family: "Montserrat", Arial, sans-serif;
    font-weight: 800;
    font-size: 25px;
    line-height: 1;
    color: var(--white);
    text-transform: uppercase;
    white-space: nowrap;
  }

  .flag {
    position: absolute;
    left: 577px; top: 384px;
    width: 188px; height: 96px;
  }

  .eoi-panel {
    position: absolute;
    left: 65px; top: 513px;
    width: 723px; height: 168px;
    border-radius: 24px;
    background: linear-gradient(180deg, #2c2c2c, #141414);
    box-shadow: 0 6px 18px rgba(0,0,0,.6);
    text-align: center;
  }
  .eoi-panel::before {
    content: "";
    position: absolute;
    inset: 14px;
    border: 2px dashed rgba(255,255,255,.55);
    border-radius: 14px;
  }
  .eoi-lead {
    position: absolute; left: 0; right: 0; top: 44px;
    font-family: "Archivo Black", Arial, sans-serif;
    font-size: 30px;
    line-height: 1;
    letter-spacing: 0.5px;
  }
  .eoi-title {
    position: absolute; left: 0; right: 0; top: 76px;
    font-family: "Archivo Black", Arial, sans-serif;
    font-size: 66px;
    line-height: 1;
    color: var(--brand-yellow);
    letter-spacing: 1px;
  }

  .tour-length {
    position: absolute; left: 0; right: 0; top: 700px;
    text-align: center;
    font-family: "Oswald", Arial, sans-serif;
    font-weight: 600;
    font-size: 96px;
    line-height: 1;
    color: var(--brand-red);
  }

  .tour-dates {
    position: absolute; left: 0; right: 0; top: 812px;
    display: flex; align-items: center; gap: 18px;
    font-family: "Montserrat", Arial, sans-serif;
    font-weight: 800;
    font-size: 21px;
    white-space: nowrap;
  }
  .tour-dates::before, .tour-dates::after {
    content: ""; flex: 1; height: 4px; background: var(--white);
  }

  .details {
    position: absolute; left: 0; top: 842px;
    width: 849px; height: 202px;
    background: var(--panel);
    text-align: center;
  }
  .audience {
    position: absolute; left: 0; right: 0; top: 24px;
    font-family: "Oswald", Arial, sans-serif;
    font-weight: 600;
    font-size: 46px;
    line-height: 1;
  }
  .audience em { font-style: normal; color: var(--brand-red); }
  .grounds {
    position: absolute; left: 0; right: 0; top: 102px;
    font-family: "Archivo Black", Arial, sans-serif;
    font-size: 30px;
    color: var(--bright-blue);
    letter-spacing: 0.5px;
  }
  .coaches {
    position: absolute; left: 0; right: 0; top: 148px;
    font-family: "Archivo Black", Arial, sans-serif;
    font-size: 19px;
    color: var(--brand-yellow);
  }

  .contact {
    position: absolute; left: 0; top: 1044px;
    width: 849px; height: 156px;
    background: var(--footer);
    border-top: 4px solid var(--rule);
    text-align: center;
  }
  .contact-line {
    margin-top: 26px;
    font-weight: 800;
    font-size: 35px;
  }
  .contact-email {
    margin-top: 6px;
    font-weight: 800;
    font-size: 33px;
    color: var(--brand-red);
  }
</style>
</head>
<body>
<main class="flyer">
  <div class="hero-scene" role="img" aria-label="Palm-lined tropical beach with sea and rocks, opening onto a floodlit cricket stadium field"></div>
  <div class="hero-flag-banner" role="img" aria-label="Sri Lankan flag waving across the sky"></div>
  <div class="hero-players" role="img" aria-label="Two teenage girls in cricket kit, one raising her bat and helmet in celebration"></div>

  <div class="brand">
    <span class="brand-dot"></span>
    <span class="brand-name">Halvey Athletics</span>
  </div>

  <svg class="flag" viewBox="0 0 188 96" role="img" aria-label="Flag of Sri Lanka">
    <rect x="0" y="0" width="188" height="96" fill="var(--flag-gold)"/>
    <rect x="7" y="7" width="26" height="82" fill="var(--flag-green)"/>
    <rect x="33" y="7" width="26" height="82" fill="var(--flag-orange)"/>
    <rect x="66" y="7" width="115" height="82" fill="var(--flag-maroon)"/>
  </svg>

  <section class="eoi-panel">
    <p class="eoi-lead">EXPRESSIONS OF</p>
    <h1 class="eoi-title">INTEREST</h1>
  </section>

  <h2 class="tour-length">10 DAY TOUR</h2>
  <p class="tour-dates">JULY 4TH TO 14TH 2018</p>

  <section class="details">
    <p class="audience">FOR <em>GIRLS</em> AGED 14 TO 18</p>
    <p class="grounds">PLAY ON FIRST CLASS GROUNDS</p>
    <p class="coaches">LEVEL 3 COACHES WITH INTERNATIONAL EXPERIENCE</p>
  </section>

  <footer class="contact">
    <p class="contact-line">For More Information Contact Boyd</p>
    <p class="contact-email">boyd@halveyathletics.com.au</p>
  </footer>
</main>
</body>
</html>
```